Infectious Diseases Research Laboratory Needs Business Card

We need a business card for an academic research laboratory based in Kansas City called MORVEK. The full lab name is Microbial Dose-Response/Exposure Bridging Studies Laboratory, but this does not need to be incorporated. We study novel ways to optimize the treatment of multidrug-resistant bacterial infections ("superbugs") throughout the entire biomedical research spectrum (from benchtop to bedside). The name MORVEK is not only an acronym for our lab name, but also represents our desire to make discoveries and explore the unknown (the stars, if you well). It also serves as an ode to the state of Kansas motto where we are based, ad astra per aspera ("to the stars, through difficulty").

Target Market(s)

Pharmaceutical companies, researchers

Industry/Entity Type

Pharmaceutical

Contact Information for Business Card

The business card should incorporate and complement our new logo (see uploaded files). Double-sided designs are preferred. Looking for something modern, but professional.

Font styles to use
Sans Serif

Requirements
Must have
• Double-sided. One side would ideally be a solid color incorporating logo and the other should also have the logo (smaller), but incorporate staff information.
• Color codes:
• Red: #F04C51
• Blue: #3477B5
• Gray: #808285

```html
<!DOCTYPE html>
<html lang="en">
<head>
<meta charset="utf-8">
<title>MORVEK Business Card</title>
<link rel="stylesheet" href="https://fonts.googleapis.com/css2?family=Source+Sans+3:wght@400;600&display=swap">
<style>
  :root {
    --page-bg: #e9e9eb;
    --blue-deep: #1c4a94;
    --blue-mid: #2b62ad;
    --blue-light: #3477b5;
    --red: #f04c51;
    --gray: #808285;
    --panel-light: #eef0f3;
    --panel-mid: #dfe3ea;
    --text-light: #ffffff;
    --text-soft: #dfe7f3;
  }
  * { margin: 0; padding: 0; box-sizing: border-box; }
  html, body {
    width: 1200px;
    height: 969px;
    overflow: hidden;
    background: var(--page-bg);
    font-family: "Source Sans 3", sans-serif;
  }
  .business-card {
    position: absolute;
    left: 100px;
    top: 200px;
    width: 1000px;
    height: 569px;
    box-shadow: 0 14px 40px rgba(0,0,0,0.22);
  }
  .card-art { position: absolute; inset: 0; display: block; }
  .staff-name {
    position: absolute;
    left: 57px;
    top: 54px;
    font-size: 25px;
    font-weight: 600;
    color: var(--text-light);
    letter-spacing: 0.5px;
  }
  .staff-title {
    position: absolute;
    left: 57px;
    top: 88px;
    font-size: 25px;
    font-weight: 400;
    color: var(--text-soft);
    letter-spacing: 0.3px;
  }
  .lab-address {
    position: absolute;
    left: 57px;
    top: 287px;
    font-size: 23px;
    line-height: 31px;
    color: var(--text-soft);
    font-style: normal;
  }
  .contact-list {
    position: absolute;
    left: 57px;
    top: 366px;
    list-style: none;
  }
  .contact-item {
    display: flex;
    align-items: center;
    height: 32px;
    font-size: 22px;
    color: var(--text-soft);
  }
  .contact-icon {
    width: 20px;
    height: 20px;
    margin-right: 14px;
    fill: var(--text-soft);
  }
  .lab-mark {
    position: absolute;
    left: 588px;
    top: 250px;
    display: flex;
    align-items: center;
  }
  .lab-mark-dot {
    width: 46px;
    height: 46px;
    border-radius: 50%;
    background: var(--blue-light);
    margin-right: 16px;
  }
  .lab-name {
    font-size: 66px;
    font-weight: 600;
    color: var(--red);
    letter-spacing: 3px;
    line-height: 1;
  }
</style>
</head>
<body>
  <section class="business-card">
    <svg class="card-art" viewBox="0 0 1000 569" width="1000" height="569">
      <defs>
        <linearGradient id="blueSide" x1="0" y1="0" x2="1" y2="1">
          <stop offset="0" stop-color="var(--blue-mid)"/>
          <stop offset="0.55" stop-color="var(--blue-deep)"/>
          <stop offset="1" stop-color="var(--blue-mid)"/>
        </linearGradient>
        <radialGradient id="frostPanel" cx="0.55" cy="0.45" r="0.7">
          <stop offset="0" stop-color="var(--panel-light)"/>
          <stop offset="1" stop-color="var(--panel-mid)"/>
        </radialGradient>
      </defs>
      <rect class="blue-side" x="0" y="0" width="1000" height="569" fill="url(#blueSide)"/>
      <path class="frost-panel" role="img" aria-label="Frosted panel with a soft pattern of scattered red and blue circles"
            d="M621,0 C480,70 395,190 405,285 C418,400 560,520 707,569 L1000,569 L1000,0 Z"
            fill="url(#frostPanel)"/>
      <path class="panel-edge" d="M621,0 C480,70 395,190 405,285 C418,400 560,520 707,569"
            fill="none" stroke="var(--red)" stroke-width="4"/>
    </svg>

    <h1 class="staff-name">NORA HALVIK</h1>
    <p class="staff-title">CEO/FOUNDER</p>

    <address class="lab-address">2140 Larkspur Court<br>Kansas City, Kansas 66103</address>

    <ul class="contact-list">
      <li class="contact-item">
        <svg class="contact-icon" viewBox="0 0 20 20"><path d="M2 7c0-3 4-4 8-4s8 1 8 4v2h-4V7H6v2H2z M4 10h12l2 7H2z"/></svg>
        913 555 0142
      </li>
      <li class="contact-item">
        <svg class="contact-icon" viewBox="0 0 20 20"><path d="M6 1h8a1 1 0 0 1 1 1v16a1 1 0 0 1-1 1H6a1 1 0 0 1-1-1V2a1 1 0 0 1 1-1zm1 2v12h6V3z"/></svg>
        913 555 0187
      </li>
      <li class="contact-item">
        <svg class="contact-icon" viewBox="0 0 20 20"><path d="M5 2h10v5H5z M2 8h16v8h-3v3H5v-3H2z M7 13v4h6v-4z"/></svg>
        913 555 0199
      </li>
      <li class="contact-item">
        <svg class="contact-icon" viewBox="0 0 20 20"><path d="M1 5h18v11H1z M2 6l8 6 8-6v-1H2z" fill-rule="evenodd"/></svg>
        nora@morvek.com
      </li>
      <li class="contact-item">
        <svg class="contact-icon" viewBox="0 0 20 20"><circle cx="10" cy="10" r="8"/><path d="M10 2v16M2 10h16" stroke="var(--blue-deep)" stroke-width="1.5"/></svg>
        www.morvek.com
      </li>
    </ul>

    <div class="lab-mark">
      <span class="lab-mark-dot"></span>
      <span class="lab-name">MORVEK</span>
    </div>
  </section>
</body>
</html>
```